Frostvale Cool Packs needs stationery designed for their new logo

We have a new logo so now want all our stationery to be redesigned.
Frostvale is a gel ice pack product used by the seafood & food industry to transport chilled products around the world.

We would like to use our new logo with icy or snow backgrounds or elements.
Our company tag line is "Keep your products chilled for longer"
I'll attach our old business cards so that you can use the text off them.
2nd attachment is our new logo to be used.

We want a design for:
- Business cards
- Letter Head
- Email signature

Target Market(s)

seafood & chilled food distributors

Industry/Entity Type

Industry

Font styles to use
Sans Serif

Colors
0492cd
85cae6
cee9f5

Requirements
Must have
• Our logo
Nice to have
• Snow or ice background or image incorporated somehow

```html
<!DOCTYPE html>
<html lang="en">
<head>
<meta charset="utf-8">
<title>Frostvale Cool Packs – Stationery</title>
<link href="https://fonts.googleapis.com/css2?family=Mulish:ital,wght@0,400;0,600;0,700;1,400&display=swap" rel="stylesheet">
<style>
  :root{
    --brand-blue:#0492cd;
    --ice-mid:#85cae6;
    --ice-pale:#cee9f5;
    --ink:#333a40;
    --grey:#8a8f94;
    --paper:#ffffff;
    --backdrop:#eef1f3;
  }
  *{box-sizing:border-box;margin:0;padding:0}
  html,body{width:1200px;height:1200px;overflow:hidden}
  body{background:var(--backdrop);font-family:"Mulish",sans-serif;color:var(--ink);position:relative}
  .sheet{position:absolute;overflow:hidden;box-shadow:0 2px 8px rgba(0,0,0,.18)}
  .ice{position:absolute;display:block}
  .frost-paper{background:radial-gradient(ellipse at 50% 55%,#ffffff 25%,#e9f5fb 70%,var(--ice-pale) 100%)}

  /* Letterhead */
  .letterhead{left:26px;top:48px;width:580px;height:821px}
  .letterhead .ice{left:0;top:0;width:580px;height:140px}
  .letterhead .tagline{position:absolute;left:352px;top:38px;font-size:14px;font-weight:600;letter-spacing:1.6px;line-height:21px;color:var(--grey);text-transform:uppercase}
  .letterhead .sender{position:absolute;left:36px;top:708px;width:200px}
  .letterhead .rule{height:1px;background:linear-gradient(90deg,var(--brand-blue),transparent);margin-bottom:8px}
  .letterhead .name{font-size:15px;font-weight:700}
  .letterhead .role{font-size:10px;font-style:italic;margin-top:2px}
  .letterhead .contact{font-size:9px;margin-top:8px;line-height:15px}
  .letterhead .web{color:var(--brand-blue);font-weight:700;letter-spacing:.5px}
  .letterhead .brand{position:absolute;left:400px;top:728px;font-size:24px;font-weight:700;color:var(--brand-blue)}

  .icon{display:inline-block;vertical-align:middle;margin-right:4px}

  /* Business cards */
  .card{background:var(--paper)}
  .card-front{left:641px;top:158px;width:507px;height:284px}
  .card-back{left:641px;top:472px;width:512px;height:291px}
  .card .ice{left:0;top:0;width:100%;height:190px}
  .card .brand{position:absolute;left:0;right:0;top:40px;text-align:center;font-size:27px;font-weight:700;color:var(--paper)}
  .card .tagline{position:absolute;left:0;right:0;top:105px;text-align:center;font-size:13px;font-weight:700;letter-spacing:.4px;color:var(--paper);text-transform:uppercase}
  .card-front .identity{position:absolute;left:40px;top:202px}
  .card-front .name{font-size:19px;font-weight:700}
  .card-front .role{font-size:12.5px;font-style:italic;color:var(--brand-blue);margin-top:2px}
  .card-front .contact{position:absolute;left:222px;top:207px;font-size:12.5px;line-height:19px}
  .card-front .web{color:var(--brand-blue);font-weight:700;letter-spacing:.6px}
  .card-back .office{position:absolute;top:205px;width:250px;text-align:center;font-size:13.5px;line-height:17px}
  .card-back .office-sydney{left:40px}
  .card-back .office-auckland{left:244px}
  .card-back .city{color:var(--brand-blue);font-weight:700;font-size:14px}
  .card-back .divider{position:absolute;left:258px;top:190px;width:2px;height:80px;background:var(--brand-blue)}

  /* Email signature */
  .signature{left:226px;top:903px;width:760px;height:255px;background:var(--paper)}
  .signature .ice-left{left:0;bottom:0;width:270px;height:92px}
  .signature .ice-right{right:0;bottom:0;width:190px;height:68px}
  .signature .brand{position:absolute;left:30px;top:82px;font-size:42px;font-weight:700;color:var(--grey)}
  .signature .brand-dot{display:inline-block;width:34px;height:34px;border-radius:50%;background:var(--brand-blue);vertical-align:-4px;margin-right:12px}
  .signature .divider{position:absolute;left:373px;top:36px;width:1.5px;height:178px;background:var(--brand-blue)}
  .signature .identity{position:absolute;left:396px;top:50px}
  .signature .name{font-size:36px;font-weight:700;line-height:44px}
  .signature .role{font-size:23px;font-style:italic;color:var(--brand-blue);margin-top:2px}
  .signature .contact{font-size:19px;line-height:28px;margin-top:10px}
  .signature .web{color:var(--brand-blue);font-weight:700;letter-spacing:1.4px}
</style>
</head>
<body>

<!-- Letterhead -->
<section class="sheet letterhead frost-paper">
  <svg class="ice" viewBox="0 0 580 140" preserveAspectRatio="none" role="img" aria-label="Icy crystal texture in bright blues along the top edge">
    <defs>
      <linearGradient id="iceLh" x1="0" y1="0" x2="1" y2="1">
        <stop offset="0" stop-color="#3aa9dc"/><stop offset=".5" stop-color="#8fd0ec"/><stop offset="1" stop-color="#1d8fc8"/>
      </linearGradient>
    </defs>
    <polygon points="0,0 338,0 300,44 262,62 228,106 172,86 126,108 98,90 70,110 46,124 26,96 0,104" fill="url(#iceLh)"/>
    <polyline points="338,0 300,44 262,62 228,106 172,86 126,108 98,90 70,110 46,124 26,96 0,104" fill="none" stroke="#0a6fa8" stroke-width="2"/>
  </svg>
  <p class="tagline">Keep your products<br>chilled for longer</p>
  <div class="sender">
    <div class="rule"></div>
    <p class="name">Dana Whitlow</p>
    <p class="role">Business Development</p>
    <p class="contact">
      <svg class="icon" width="9" height="7" viewBox="0 0 9 7"><rect width="9" height="7" fill="#333a40"/><polyline points="0,0 4.5,4 9,0" fill="none" stroke="#fff" stroke-width="1"/></svg>dana.whitlow@frostvale.com.au<br>
      <svg class="icon" width="9" height="9" viewBox="0 0 10 10"><circle cx="5" cy="5" r="4" fill="none" stroke="#0492cd" stroke-width="2"/></svg><span class="web">www.frostvale.com.au</span>
    </p>
  </div>
  <p class="brand">Frostvale</p>
</section>

<!-- Business card front -->
<section class="sheet card card-front">
  <svg class="ice" viewBox="0 0 507 190" preserveAspectRatio="none" role="img" aria-label="Icy crystal texture in bright blues">
    <defs>
      <linearGradient id="iceCf" x1="0" y1="0" x2="1" y2="1">
        <stop offset="0" stop-color="#2a9fd6"/><stop offset=".45" stop-color="#7cc6e8"/><stop offset="1" stop-color="#0f86c3"/>
      </linearGradient>
    </defs>
    <polygon points="0,0 507,0 507,185 488,168 460,176 428,130 372,188 338,140 302,148 262,132 226,174 184,164 150,142 118,186 72,152 42,168 20,118 0,124" fill="url(#iceCf)"/>
  </svg>
  <p class="brand">Frostvale</p>
  <p class="tagline">Keep your products chilled for longer</p>
  <div class="identity">
    <p class="name">Dana Whitlow</p>
    <p class="role">Business Development</p>
  </div>
  <p class="contact">
    <svg class="icon" width="11" height="8" viewBox="0 0 9 7"><rect width="9" height="7" fill="#333a40"/><polyline points="0,0 4.5,4 9,0" fill="none" stroke="#fff" stroke-width="1"/></svg>dana.whitlow@frostvale.com.au<br>
    <svg class="icon" width="11" height="11" viewBox="0 0 10 10"><circle cx="5" cy="5" r="4" fill="none" stroke="#0492cd" stroke-width="2"/></svg><span class="web">www.frostvale.com.au</span>
  </p>
</section>

<!-- Business card back -->
<section class="sheet card card-back">
  <svg class="ice" viewBox="0 0 512 190" preserveAspectRatio="none" role="img" aria-label="Close-up of clear blue ice shards">
    <defs>
      <linearGradient id="iceCb" x1="0" y1="0" x2="1" y2="1">
        <stop offset="0" stop-color="#5fbbe4"/><stop offset=".5" stop-color="#a8dcf2"/><stop offset="1" stop-color="#1b92cc"/>
      </linearGradient>
    </defs>
    <polygon points="0,0 512,0 512,188 488,168 454,176 424,130 372,188 338,146 300,140 240,136 196,178 154,172 110,134 68,188 44,162 20,128 0,126" fill="url(#iceCb)"/>
  </svg>
  <p class="brand">Frostvale</p>
  <p class="tagline">Keep your products chilled for longer</p>
  <div class="office office-sydney">
    <p class="city">SYDNEY</p>
    <p>18 Kelp Street,<br>North Sydney, NSW 2060</p>
  </div>
  <div class="divider"></div>
  <div class="office office-auckland">
    <p class="city">AUCKLAND</p>
    <p>5 Tide Road, Silverdale<br>Auckland 0932</p>
  </div>
</section>

<!-- Email signature -->
<section class="sheet signature">
  <svg class="ice ice-left" viewBox="0 0 270 92" preserveAspectRatio="none" role="img" aria-label="Icy crystal texture in bright blues">
    <defs>
      <linearGradient id="iceSl" x1="0" y1="0" x2="1" y2="1">
        <stop offset="0" stop-color="#2a9fd6"/><stop offset=".5" stop-color="#7cc6e8"/><stop offset="1" stop-color="#0f86c3"/>
      </linearGradient>
    </defs>
    <polygon points="0,30 24,12 44,30 68,22 100,42 126,26 166,20 186,46 228,58 246,80 262,92 0,92" fill="url(#iceSl)"/>
  </svg>
  <svg class="ice ice-right" viewBox="0 0 190 68" preserveAspectRatio="none" role="img" aria-label="Icy crystal texture in bright blues">
    <defs>
      <linearGradient id="iceSr" x1="0" y1="0" x2="1" y2="1">
        <stop offset="0" stop-color="#2a9fd6"/><stop offset=".5" stop-color="#7cc6e8"/><stop offset="1" stop-color="#0f86c3"/>
      </linearGradient>
    </defs>
    <polygon points="0,68 30,46 56,44 82,12 112,24 140,20 162,0 190,20 190,68" fill="url(#iceSr)"/>
  </svg>
  <p class="brand"><span class="brand-dot"></span>Frostvale</p>
  <div class="divider"></div>
  <div class="identity">
    <p class="name">Dana Whitlow</p>
    <p class="role">Business Development</p>
    <p class="contact">
      <svg class="icon" width="18" height="13" viewBox="0 0 9 7"><rect width="9" height="7" fill="#333a40"/><polyline points="0,0 4.5,4 9,0" fill="none" stroke="#fff" stroke-width=".8"/></svg>dana.whitlow@frostvale.com.au<br>
      <svg class="icon" width="17" height="17" viewBox="0 0 10 10"><circle cx="5" cy="5" r="4" fill="none" stroke="#0492cd" stroke-width="1.8"/></svg><span class="web">www.frostvale.com.au</span>
    </p>
  </div>
</section>

</body>
</html>
```